Self Watering Planter Packaging

We would like to create a unique Retail Packaging for our Self Watering Planter.
It is a Cedar Planter that is a Self Watering Cedar Planter that has a fountain.
It has a long lasting battery that last 3 months watering every other day.
Programable Automatic Watering System
Fountain Oxygenates the water Keeping the fresh water flowing and prevents stagnate smelly water.
No more root Rot because the System Aerates the Roots every time you water. Just like it does in nature.
Patented System that waters from the bottom up
No Power Cords
No Solar Panels
No Plumbing
I have put the old packaging that we had for our first version. We want something much better than this. We want this to be slanted to urban living, and being able to grow anywhere,
This system is guaranteed to grow amazing plants, fruits and vegetables.
Packaging size will be 36"L x 4"x12"
We will want a matching sell sheet to go along with this as well.
Reason: I have extended the Deadline
Target Market(s)
Anyone that likes to garden but may not have the land to garden. Herb Gardens, Urban Gardens, etc.
Industry/Entity Type
Retail
Look and feel

```html
<!DOCTYPE html>
<html lang="en">
<head>
<meta charset="utf-8">
<title>Farmer Ray's Grow Engine – Retail Box Dieline</title>
<link href="https://fonts.googleapis.com/css2?family=Oswald:wght@500&family=Roboto+Condensed:wght@400;700&display=swap" rel="stylesheet">
<style>
  :root{
    --brand-green:#13875a;
    --brand-green-dark:#0e7049;
    --paper:#ffffff;
    --brick-light:#e6e6e6;
    --brick-mid:#c9c9c9;
    --cedar:#c99a62;
    --foliage:#6f8f4e;
    --ink-white:#ffffff;
  }
  html,body{margin:0;padding:0;width:1038px;height:1200px;overflow:hidden;background:var(--paper);}
  .dieline{position:absolute;left:0;top:307px;width:1038px;height:586px;display:block;}
  .brand-name{font-family:"Oswald",sans-serif;font-weight:500;}
  .caption{font-family:"Roboto Condensed",sans-serif;font-weight:400;}
  .label-bold{font-family:"Roboto Condensed",sans-serif;font-weight:700;}
</style>
</head>
<body>
<svg class="dieline" viewBox="90 80 1120 632" xmlns="http://www.w3.org/2000/svg" role="group" aria-label="Flat box dieline for the Farmer Ray's Grow Engine self watering cedar planter">
  <defs>
    <linearGradient id="brickGrad" x1="0" y1="0" x2="0" y2="1">
      <stop offset="0" stop-color="var(--brick-light)"/>
      <stop offset="0.7" stop-color="#dadada"/>
      <stop offset="1" stop-color="var(--brick-mid)"/>
    </linearGradient>
    <linearGradient id="planterGrad" x1="0" y1="0" x2="0" y2="1">
      <stop offset="0" stop-color="var(--foliage)"/>
      <stop offset="0.45" stop-color="#8a9a6a"/>
      <stop offset="0.5" stop-color="var(--cedar)"/>
      <stop offset="1" stop-color="#b58654"/>
    </linearGradient>
    <clipPath id="frontClip"><rect x="330" y="195" width="640" height="212"/></clipPath>
    <path id="badgeTop" d="M528 365 A37 37 0 0 1 602 365"/>
    <path id="badgeBottom" d="M522 365 A43 43 0 0 0 608 365"/>

    <!-- icon set -->
    <symbol id="iconFountain" viewBox="0 0 24 24"><circle cx="12" cy="12" r="12" fill="var(--ink-white)"/><rect x="6" y="14" width="12" height="4" fill="var(--brand-green)"/><path d="M12 14V7M12 8Q8 6 7 11M12 8Q16 6 17 11" stroke="var(--brand-green)" stroke-width="1.6" fill="none"/></symbol>
    <symbol id="iconDrop" viewBox="0 0 24 24"><circle cx="12" cy="12" r="12" fill="var(--ink-white)"/><path d="M12 4Q6 12 7.5 15A4.5 4.5 0 0 0 16.5 15Q18 12 12 4Z" fill="var(--brand-green)"/></symbol>
    <symbol id="iconBattery" viewBox="0 0 24 24"><circle cx="12" cy="12" r="12" fill="var(--ink-white)"/><rect x="7" y="5" width="10" height="15" rx="1.5" fill="var(--brand-green)"/><rect x="10" y="3.5" width="4" height="2" fill="var(--brand-green)"/><text x="12" y="15" text-anchor="middle" class="label-bold" font-size="7" fill="var(--ink-white)">3</text></symbol>
    <symbol id="iconScreen" viewBox="0 0 24 24"><circle cx="12" cy="12" r="12" fill="var(--ink-white)"/><rect x="5" y="6" width="14" height="10" rx="1" fill="var(--brand-green)"/><rect x="9" y="17" width="6" height="2" fill="var(--brand-green)"/><path d="M8 9h8M8 12h5" stroke="var(--ink-white)" stroke-width="1.2"/></symbol>
    <symbol id="iconNoSolar" viewBox="0 0 24 24"><circle cx="12" cy="12" r="12" fill="var(--ink-white)"/><path d="M5 17L8 10H18L15 17Z" fill="var(--brand-green)"/><circle cx="8" cy="8" r="2.5" fill="var(--brand-green)"/><circle cx="19" cy="5" r="3.5" fill="var(--brand-green)"/><path d="M17.5 3.5l3 3M20.5 3.5l-3 3" stroke="var(--ink-white)" stroke-width="1"/></symbol>
    <symbol id="iconNoPlug" viewBox="0 0 24 24"><circle cx="12" cy="12" r="12" fill="var(--ink-white)"/><rect x="8" y="9" width="8" height="6" rx="1" fill="var(--brand-green)"/><path d="M10 9V6M14 9V6M12 15V20" stroke="var(--brand-green)" stroke-width="1.6"/><circle cx="19" cy="5" r="3.5" fill="var(--brand-green)"/><path d="M17.5 3.5l3 3M20.5 3.5l-3 3" stroke="var(--ink-white)" stroke-width="1"/></symbol>
    <symbol id="iconNoTap" viewBox="0 0 24 24"><circle cx="12" cy="12" r="12" fill="var(--ink-white)"/><path d="M5 10H14V13H17V18H14V15H5Z" fill="var(--brand-green)"/><rect x="8" y="7" width="3" height="3" fill="var(--brand-green)"/><circle cx="19" cy="5" r="3.5" fill="var(--brand-green)"/><path d="M17.5 3.5l3 3M20.5 3.5l-3 3" stroke="var(--ink-white)" stroke-width="1"/></symbol>

    <!-- top flap artwork (reused on bottom band, turned) -->
    <g id="flapArt">
      <use href="#iconNoSolar" x="366" y="140" width="24" height="24"/>
      <text x="378" y="172" text-anchor="middle" class="caption" font-size="4" fill="var(--ink-white)">NO POWER CORDS</text>
      <use href="#iconNoPlug" x="416" y="140" width="24" height="24"/>
      <text x="428" y="172" text-anchor="middle" class="caption" font-size="4" fill="var(--ink-white)">NO SOLAR PANELS</text>
      <use href="#iconNoTap" x="468" y="140" width="24" height="24"/>
      <text x="480" y="172" text-anchor="middle" class="caption" font-size="4" fill="var(--ink-white)">NO PLUMBING</text>
      <text x="650" y="150" text-anchor="middle" class="brand-name" font-size="20" fill="var(--ink-white)">Farmer Ray's</text>
      <text x="650" y="157" text-anchor="middle" class="caption" font-size="3.5" fill="var(--ink-white)">PATENT PENDING</text>
      <text x="650" y="176" text-anchor="middle" class="brand-name" font-size="17" fill="var(--ink-white)">GROW ENGINE</text>
      <use href="#iconFountain" x="800" y="138" width="20" height="20"/>
      <text x="810" y="166" text-anchor="middle" class="caption" font-size="3.5" fill="var(--ink-white)">Keep Your Water Fresh</text>
      <use href="#iconDrop" x="848" y="138" width="20" height="20"/>
      <text x="858" y="166" text-anchor="middle" class="caption" font-size="3.5" fill="var(--ink-white)">Water Aeration</text>
      <use href="#iconBattery" x="893" y="138" width="20" height="20"/>
      <text x="903" y="166" text-anchor="middle" class="caption" font-size="3.5" fill="var(--ink-white)">Long Battery Life</text>
      <use href="#iconScreen" x="938" y="138" width="20" height="20"/>
      <text x="948" y="166" text-anchor="middle" class="caption" font-size="3.5" fill="var(--ink-white)">Programable System</text>
    </g>

    <!-- main face artwork (reused on back face, turned) -->
    <g id="faceArt">
      <g clip-path="url(#frontClip)">
        <rect x="330" y="195" width="640" height="212" fill="url(#brickGrad)" role="img" aria-label="Photo of a white brick wall over a weathered grey plank floor"/>
        <rect x="445" y="200" width="220" height="207" rx="6" fill="url(#planterGrad)" role="img" aria-label="Photo of the cedar planter on legs filled with herbs and wildflowers"/>
        <path d="M330 195H388Q412 301 388 407H330Z" fill="var(--brand-green)"/>
      </g>
      <use href="#iconFountain" x="357" y="210" width="26" height="26"/>
      <text class="caption" font-size="4.5" fill="var(--ink-white)" text-anchor="middle"><tspan x="370" y="243">Keep Your Water Fresh</tspan><tspan x="370" y="248">With Fountain Oxygenates System</tspan></text>
      <use href="#iconDrop" x="357" y="260" width="26" height="26"/>
      <text class="caption" font-size="4.5" fill="var(--ink-white)" text-anchor="middle"><tspan x="370" y="293">Water Aeration</tspan><tspan x="370" y="298">(No More Rotten Root)</tspan></text>
      <use href="#iconBattery" x="357" y="312" width="26" height="26"/>
      <text class="caption" font-size="4.5" fill="var(--ink-white)" text-anchor="middle"><tspan x="370" y="345">Long Lasting Battery Life</tspan><tspan x="370" y="350">(3 Month NON-STOP)</tspan></text>
      <use href="#iconScreen" x="357" y="360" width="26" height="26"/>
      <text class="caption" font-size="4.5" fill="var(--ink-white)" text-anchor="middle"><tspan x="370" y="393">Programable Automatic</tspan><tspan x="370" y="398">Watering System</tspan></text>

      <circle cx="565" cy="365" r="48" fill="var(--brand-green)"/>
      <circle cx="565" cy="365" r="28" fill="#8d8d86" role="img" aria-label="Close-up photo of the fountain reservoir"/>
      <text class="label-bold" font-size="10" fill="var(--ink-white)"><textPath href="#badgeTop" startOffset="50%" text-anchor="middle">SELF WATERING</textPath></text>
      <text class="label-bold" font-size="10" fill="var(--ink-white)"><textPath href="#badgeBottom" startOffset="50%" text-anchor="middle">CEDAR PLANTER</textPath></text>

      <text x="820" y="262" text-anchor="middle" class="brand-name" font-size="36" fill="var(--brand-green)">Farmer Ray's</text>
      <text x="820" y="275" text-anchor="middle" class="label-bold" font-size="5.5" fill="var(--brand-green)">PATENT PENDING</text>
      <text x="820" y="305" text-anchor="middle" class="brand-name" font-size="31" fill="var(--brand-green)">GROW ENGINE</text>

      <g class="no-icons">
        <circle cx="776" cy="356" r="17" fill="var(--brand-green)"/>
        <use href="#iconNoSolar" x="763" y="343" width="26" height="26"/>
        <rect x="756" y="374" width="42" height="11" fill="var(--brand-green)"/>
        <text x="777" y="382" text-anchor="middle" class="label-bold" font-size="6" fill="var(--ink-white)">NO POWER CORDS</text>
        <circle cx="818" cy="356" r="17" fill="var(--brand-green)"/>
        <use href="#iconNoPlug" x="805" y="343" width="26" height="26"/>
        <rect x="800" y="374" width="42" height="11" fill="var(--brand-green)"/>
        <text x="821" y="382" text-anchor="middle" class="label-bold" font-size="6" fill="var(--ink-white)">NO SOLAR PANELS</text>
        <circle cx="862" cy="356" r="17" fill="var(--brand-green)"/>
        <use href="#iconNoTap" x="849" y="343" width="26" height="26"/>
        <rect x="846" y="374" width="38" height="11" fill="var(--brand-green)"/>
        <text x="865" y="382" text-anchor="middle" class="label-bold" font-size="6" fill="var(--ink-white)">NO PLUMBING</text>
      </g>
    </g>
  </defs>

  <!-- top glue flap with side tabs -->
  <g class="top-flap">
    <path d="M308 124L330 118V178H308Z" fill="var(--brand-green-dark)"/>
    <path d="M992 124L970 118V178H992Z" fill="var(--brand-green-dark)"/>
    <path d="M330 108Q330 100 338 100H962Q970 100 970 108V178H330Z" fill="var(--brand-green)"/>
    <use href="#flapArt"/>
  </g>

  <!-- dust tabs beside the main face -->
  <path d="M308 190H330V407H308Z" fill="var(--brand-green-dark)"/>
  <path d="M992 190H970V407H992Z" fill="var(--brand-green-dark)"/>
  <rect x="330" y="180" width="640" height="15" fill="var(--brand-green)"/>

  <!-- main face -->
  <use href="#faceArt"/>

  <!-- bottom band with end panels -->
  <g class="base-band">
    <rect x="115" y="408" width="1070" height="70" fill="var(--brand-green)"/>
    <line x1="330" y1="408" x2="330" y2="478" stroke="var(--brand-green-dark)" stroke-width="1"/>
    <line x1="970" y1="408" x2="970" y2="478" stroke="var(--brand-green-dark)" stroke-width="1"/>
    <use href="#flapArt" transform="rotate(180 650 301)"/>
    <g class="end-panel">
      <text x="222" y="440" text-anchor="middle" class="brand-name" font-size="22" fill="var(--ink-white)">Farmer Ray's</text>
      <text x="222" y="462" text-anchor="middle" class="brand-name" font-size="18" fill="var(--ink-white)">GROW ENGINE</text>
    </g>
    <g class="end-panel">
      <text x="1078" y="440" text-anchor="middle" class="brand-name" font-size="22" fill="var(--ink-white)">Farmer Ray's</text>
      <text x="1078" y="462" text-anchor="middle" class="brand-name" font-size="18" fill="var(--ink-white)">GROW ENGINE</text>
    </g>
  </g>

  <!-- back face -->
  <use href="#faceArt" transform="rotate(180 650 443.5)"/>
</svg>
</body>
</html>
```